Author/ Speaker Business Card design

I need a business card designed that will go with the branding that is already on my book and website. I like clean and straightforward, but I am not opposed to something more 'innovative'.

Target Market(s)

Colleges and Universities, educational institutions

Industry/Entity Type

Education

Contact Information for Business Card

Standard size. It should be able to be printed on good quality white or ivory paper.

Font styles to use
Sans Serif

Colors
0355a3

Requirements
Must have
• There's a blue on my website. It should have some blue. My logo is at the top. It should have the logo incorporated somewhere on it. My name, Author | Speaker | Teacher | Trainer, my phone number (+31 64-207 5819), my email address (milo@theboldlearner.example), Social media icons (twitter, Instagram, LinkedIn) with the addresses (twitter @writermilofenwick, Instagram - theboldlearner, LinkedIn - theboldlearner) By they way, the website is www.theboldlearner.example. There is a photo of the book on the website. Also, my full name is Milo Fenwick
Nice to have
• Try to use the font that is on the website and book. Also, if you could get that blue, that would be great.
Should not have
• My photo

```html
<!DOCTYPE html>
<html lang="en">
<head>
<meta charset="utf-8">
<title>Milo Fenwick – Business Card</title>
<link href="https://fonts.googleapis.com/css2?family=Questrial&display=swap" rel="stylesheet">
<style>
  :root {
    --brand-blue: #0355a3;
    --ribbon-blue: #02478a;
    --fold-blue: #013468;
    --paper: #f7f7f5;
    --stage: #2b2b2b;
    --white: #ffffff;
  }
  * { margin: 0; padding: 0; box-sizing: border-box; }
  html, body {
    width: 1200px; height: 869px; overflow: hidden;
    background: var(--stage);
    font-family: "Questrial", "Helvetica Neue", Arial, sans-serif;
  }
  .card {
    position: absolute; top: 160px;
    width: 320px; height: 548px;
    background: var(--paper);
    overflow: hidden;
  }
  .card--front { left: 240px; }
  .card--back  { left: 640px; }

  .brand {
    position: absolute; left: 0; right: 0;
    display: flex; align-items: center; justify-content: center; gap: 10px;
    color: var(--brand-blue);
    font-size: 27px; letter-spacing: 0.2px;
  }
  .brand__mark { width: 16px; height: 16px; background: var(--brand-blue); }
  .card--front .brand { top: 178px; }
  .card--back  .brand { top: 128px; }

  .panel { position: absolute; background: var(--brand-blue); }
  .card--front .panel { left: 72px; top: 258px; right: 0; bottom: 0; }
  .card--back  .panel { left: 0; top: 238px; right: 48px; bottom: 0; }

  .ribbon {
    position: absolute; left: 36px; top: 236px; right: 0; height: 76px;
    background: var(--ribbon-blue);
    color: var(--white);
    padding: 14px 0 0 22px;
  }
  .ribbon__fold { position: absolute; left: 36px; top: 312px; }
  .name {
    font-size: 21px; letter-spacing: 7px; text-transform: uppercase;
  }
  .roles {
    margin-top: 8px; font-size: 8.5px; letter-spacing: 0.8px; text-transform: uppercase;
  }

  .contact-list {
    position: absolute; list-style: none; color: var(--white);
    font-size: 12.5px;
  }
  .card--front .contact-list { left: 96px; top: 360px; }
  .card--back  .contact-list { left: 30px; top: 318px; }
  .contact-list li {
    display: flex; align-items: center; gap: 12px; height: 22px; margin-bottom: 30px;
  }
  .contact-icon { width: 14px; height: 14px; flex: none; }
  .social-dot { width: 13px; height: 13px; background: var(--white); flex: none; border-radius: 2px; }
</style>
</head>
<body>

<section class="card card--front" aria-label="Card front">
  <div class="brand"><span class="brand__mark"></span>The Bold Learner</div>
  <div class="panel"></div>
  <svg class="ribbon__fold" width="36" height="18" viewBox="0 0 36 18">
    <polygon points="0,0 36,0 36,18" fill="var(--fold-blue)"/>
  </svg>
  <div class="ribbon">
    <div class="name">Milo Fenwick</div>
    <div class="roles">Author | Speaker | Teacher | Trainer</div>
  </div>
  <ul class="contact-list">
    <li>
      <svg class="contact-icon" viewBox="0 0 16 16" aria-hidden="true">
        <path d="M2 5 Q8 1 14 5 L12 7 L10 5.5 H6 L4 7 Z" fill="#fff"/>
        <rect x="3" y="8" width="10" height="6" rx="1" fill="#fff"/>
      </svg>
      +31 64-207 5819
    </li>
    <li>
      <svg class="contact-icon" viewBox="0 0 16 16" aria-hidden="true">
        <rect x="1" y="3" width="14" height="10" fill="none" stroke="#fff" stroke-width="1.4"/>
        <polyline points="1,3 8,9 15,3" fill="none" stroke="#fff" stroke-width="1.4"/>
      </svg>
      milo@theboldlearner.example
    </li>
    <li>
      <svg class="contact-icon" viewBox="0 0 16 16" aria-hidden="true">
        <circle cx="8" cy="8" r="6.3" fill="none" stroke="#fff" stroke-width="1.2"/>
        <ellipse cx="8" cy="8" rx="2.8" ry="6.3" fill="none" stroke="#fff" stroke-width="1"/>
        <line x1="1.7" y1="8" x2="14.3" y2="8" stroke="#fff" stroke-width="1"/>
      </svg>
      theboldlearner.example
    </li>
  </ul>
</section>

<section class="card card--back" aria-label="Card back">
  <div class="brand"><span class="brand__mark"></span>The Bold Learner</div>
  <div class="panel"></div>
  <ul class="contact-list">
    <li><span class="social-dot"></span>@writermilofenwick</li>
    <li><span class="social-dot"></span>theboldlearner</li>
    <li><span class="social-dot"></span>theboldlearner</li>
  </ul>
</section>

</body>
</html>
```